Branding for Clearflow Honours program collateral

The Clearflow Honours, hosted by the Aqueduct Trade Union, are an annual awards program to recognise excellence in the Australian water industry. The awards presentation ceremony is held over a formal luncheon, with a MC and Keynote Speaker. The awards event is a premium experience for business professionals that work in the work sector. It is a corporate business luncheon with management level professionals in attendance. We are seeking branding design elements that we can use on all awards collateral including the website, printed invitation, event program, social media posts etc. The Clearflow Honours are well known in the industry and recognised by its logo and corporate colours (attached). We would like these incorporated into the design.

Target Market(s)

business professionals

Industry/Entity Type

Water Company

Requirements
Must have
• event logo, corporate colours

```html
<!DOCTYPE html>
<html lang="en">
<head>
<meta charset="utf-8">
<title>Clearflow Honours – Event image options</title>
<link href="https://fonts.googleapis.com/css2?family=Montserrat:wght@500;600&family=Ubuntu:wght@300;400&display=swap" rel="stylesheet">
<style>
  :root {
    --board: #dfe0e2;
    --label: #2ab0c8;
    --teal: #22b0c8;
    --teal-deep: #1a7fb0;
    --splash-blue: #6aa6dc;
    --gold-light: #dcc37d;
    --gold-mid: #c9ad68;
    --gold-dark: #9f864a;
    --white: #ffffff;
  }
  * { box-sizing: border-box; margin: 0; padding: 0; }
  html, body { width: 1200px; height: 1200px; overflow: hidden; }
  body {
    background: var(--board);
    position: relative;
    font-family: "Ubuntu", sans-serif;
  }

  .option-label {
    position: absolute;
    color: var(--label);
    font: 300 18px/23px "Ubuntu", sans-serif;
  }
  .option-number {
    position: absolute;
    color: var(--label);
    font: 300 46px/1 "Ubuntu", sans-serif;
  }

  .event-image {
    position: absolute;
    width: 356px;
    height: 358px;
    overflow: hidden;
    background: var(--white);
  }
  .block { position: absolute; }
  .gold { background: linear-gradient(90deg, var(--gold-light) 0%, var(--gold-light) 45%, var(--gold-mid) 70%, var(--gold-dark) 100%); }
  .teal { background: var(--teal); }

  .splash {
    position: absolute;
    border-radius: 50%;
  }
  .splash--white {
    background: radial-gradient(ellipse at center, rgba(255,255,255,.95) 0%, rgba(255,255,255,.8) 35%, rgba(40,120,190,.45) 60%, rgba(34,176,200,0) 75%);
  }
  .splash--blue {
    background: radial-gradient(ellipse at center, rgba(106,166,220,.75) 0%, rgba(106,166,220,.45) 45%, rgba(106,166,220,0) 72%);
  }

  .event-name {
    position: absolute;
    left: 0; right: 0;
    text-align: center;
    font-family: "Montserrat", sans-serif;
    font-weight: 500;
    color: var(--white);
    letter-spacing: .5px;
  }
  .event-place {
    position: absolute;
    left: 0; right: 0;
    text-align: center;
    font-family: "Montserrat", sans-serif;
    font-weight: 500;
    color: var(--white);
    letter-spacing: 2px;
    text-transform: uppercase;
  }
  .on-white { color: var(--teal); }

  .year-ring {
    position: absolute;
    border-radius: 50%;
    border: 4px solid var(--gold-mid);
    box-shadow: 2px 3px 4px rgba(0,0,0,.2);
    display: flex;
    align-items: center;
    justify-content: center;
    font-family: "Ubuntu", sans-serif;
    font-weight: 300;
    letter-spacing: 1px;
  }
</style>
</head>
<body>

  <!-- Option 1 -->
  <p class="option-label" style="left:104px;top:48px;">Event image -<br>360px x 360px</p>
  <span class="option-number" style="left:104px;top:110px;">1</span>
  <section class="event-image" style="left:186px;top:117px;">
    <div class="block gold" style="left:0;top:0;width:356px;height:180px;"></div>
    <div class="block teal" style="left:0;top:180px;width:356px;height:178px;"></div>
    <div class="splash splash--blue" role="img" aria-label="Blue water splash over the gold band" style="left:150px;top:-20px;width:240px;height:200px;"></div>
    <div class="splash splash--white" role="img" aria-label="White water splash bursting from the lower right" style="left:180px;top:220px;width:220px;height:170px;"></div>
    <p class="event-name" style="top:60px;font-size:24px;">Clearflow Honours</p>
    <p class="event-place" style="top:100px;font-size:9px;">South Australia</p>
    <div class="year-ring" style="left:269px;top:135px;width:60px;height:60px;border-width:3px;color:var(--white);font-size:15px;">2019</div>
  </section>

  <!-- Option 2 -->
  <p class="option-label" style="left:623px;top:134px;">Event image -<br>360px x 360px</p>
  <span class="option-number" style="left:624px;top:196px;">2</span>
  <section class="event-image" style="left:666px;top:186px;">
    <div class="block gold" style="left:0;top:0;width:356px;height:139px;"></div>
    <div class="block teal" style="left:0;top:166px;width:356px;height:192px;"></div>
    <div class="splash splash--white" role="img" aria-label="White water splash bursting from the lower right" style="left:180px;top:210px;width:220px;height:170px;"></div>
    <p class="event-name" style="top:32px;font-size:24px;">Clearflow Honours</p>
    <p class="event-place" style="top:80px;font-size:9px;">South Australia</p>
    <div class="year-ring" style="left:250px;top:86px;width:92px;height:92px;color:var(--white);font-weight:500;font-size:17px;background:linear-gradient(180deg, transparent 58%, var(--white) 58%);">
      <span style="margin-top:-14px;">2019</span>
    </div>
  </section>

  <!-- Option 3 -->
  <p class="option-label" style="left:154px;top:560px;">Event image -<br>360px x 360px</p>
  <span class="option-number" style="left:154px;top:622px;">3</span>
  <section class="event-image" style="left:190px;top:625px;">
    <div class="block gold" style="left:0;top:176px;width:183px;height:182px;"></div>
    <div class="block teal" style="left:183px;top:176px;width:173px;height:182px;"></div>
    <div class="splash splash--blue" role="img" aria-label="Blue water splash flowing across the gold panel" style="left:20px;top:200px;width:220px;height:160px;"></div>
    <div class="splash splash--white" role="img" aria-label="White water splash bursting on the teal panel" style="left:190px;top:200px;width:190px;height:170px;"></div>
    <p class="event-name on-white" style="top:38px;font-size:22px;">Clearflow Honours</p>
    <p class="event-place on-white" style="top:80px;font-size:9px;">South Australia</p>
    <div class="year-ring" style="left:251px;top:85px;width:72px;height:72px;color:var(--teal);font-size:16px;">2019</div>
  </section>

  <!-- Option 4 -->
  <p class="option-label" style="left:654px;top:632px;">Event image -<br>360px x 360px</p>
  <span class="option-number" style="left:654px;top:694px;">4</span>
  <section class="event-image" style="left:694px;top:696px;">
    <div class="block gold" style="left:0;top:0;width:183px;height:176px;"></div>
    <div class="block teal" style="left:183px;top:176px;width:173px;height:182px;"></div>
    <div class="splash splash--blue" role="img" aria-label="Blue water splash at the edge of the gold panel" style="left:110px;top:30px;width:110px;height:130px;"></div>
    <div class="splash splash--white" role="img" aria-label="White water splash bursting on the teal panel" style="left:195px;top:200px;width:180px;height:160px;"></div>
    <p class="event-name" style="top:24px;width:183px;font-size:12px;font-weight:600;">Clearflow Honours</p>
    <p class="event-place" style="top:46px;width:183px;font-size:5px;letter-spacing:1px;">South Australia</p>
    <div class="year-ring" style="left:216px;top:34px;width:88px;height:88px;color:var(--teal);font-size:19px;border-color:var(--gold-mid) var(--teal-deep) var(--teal-deep) var(--gold-mid);">2019</div>
  </section>

</body>
</html>
```